Business Card Design Project

We need a business card design for a management consultancy focused on financial innovation and digital money, run by experts from the Financial Services, Telecoms and Money Transfer industries.
Our products include services such as Mobile Payments, Mobile Money, Digital Wallets, Online Payments, Branchless Banking and more. We work with regulatory information, business plans, financial modelling, strategic planning, new products functional specification, new technologies evaluation, etc.
See company logo attached.
We would like to see 2 versions: one in portuguese and one in english (regarding data information). You can see below information needed (whenever there is a difference between the two versions, the first one is in english and the second one in portuguese).

Name
Position
Phone/ Tel: ++55-11-xxxx-xxxx
Cell/ Cel: ++55-11-9 xxxx-xxxx
Dr. Olavo Brendim Av., 312 - Tower II - 16th floor / Avenida Dr. Olavo Brendim, 312 - Torre II - 16o. andar
São Paulo - SP
06217-318 - Brazil/ 06217-318 - Brasil

Reason: 5 days to receive designs.

Target Market(s)

Audience: C-level executives from banks, credit card companies, acquirers, IT developers, retailers

Industry/Entity Type

Financial

Requirements
Must have
• Must use the logo and information above. Front must have white background. Back side should have only logo.
Nice to have
• Back should be in another colour but if it seems too exxagerated, maintain back in white also.
Should not have
• Do not add other illustrations to the business card.

```html
<!DOCTYPE html>
<html lang="en">
<head>
<meta charset="utf-8">
<title>R Marlowe Consulting – Business Card</title>
<link href="https://fonts.googleapis.com/css2?family=Ubuntu:wght@400;500;700&display=swap" rel="stylesheet">
<style>
  :root {
    --backdrop: #e6e6e9;
    --card-white: #ffffff;
    --brand-indigo: #2f2a72;
    --brand-deep: #1d1a36;
    --ink: #1c1c24;
  }
  * { box-sizing: border-box; margin: 0; padding: 0; }
  html, body {
    width: 1200px; height: 873px; overflow: hidden;
    background: var(--backdrop);
  }
  .stage {
    width: 1200px; height: 873px;
    display: flex; align-items: center; justify-content: center; gap: 60px;
  }
  .card {
    position: relative;
    width: 530px; height: 310px;
    border-radius: 3px;
    overflow: hidden;
    box-shadow: 0 4px 14px rgba(0,0,0,.18);
  }

  /* Company name placeholder */
  .brand {
    position: absolute;
    display: flex; align-items: center; gap: 10px;
    font-family: "Ubuntu", sans-serif;
    font-weight: 500;
    line-height: 1;
    white-space: nowrap;
  }
  .brand__mark { flex: none; background: currentColor; }

  /* Front */
  .card--front { background: var(--card-white); }
  .card--front .brand {
    left: 150px; top: 52px;
    color: var(--ink);
    font-size: 24px;
  }
  .card--front .brand__mark { width: 14px; height: 14px; }

  .holder {
    position: absolute; left: 46px; top: 128px;
    font-family: "Ubuntu", sans-serif;
  }
  .holder__name { font-size: 25px; font-weight: 700; color: var(--brand-indigo); line-height: 1.1; }
  .holder__role { font-size: 10px; font-weight: 700; color: var(--ink); letter-spacing: .3px; }

  .contacts {
    position: absolute; left: 250px; top: 148px;
    list-style: none;
    font-family: "Ubuntu", sans-serif; font-size: 13.5px; font-weight: 500;
    color: var(--brand-indigo);
  }
  .contacts li { display: flex; align-items: center; gap: 8px; height: 21px; white-space: nowrap; }
  .contacts li.contacts__cont { padding-left: 22px; }
  .contacts svg { width: 14px; height: 14px; flex: none; }

  .edge-band {
    position: absolute; left: 0; right: 0; bottom: 0; height: 20px;
    display: flex;
  }
  .edge-band__dark { width: 42%; background: var(--brand-deep); }
  .edge-band__color { flex: 1; background: var(--brand-indigo); }

  /* Back */
  .card--back {
    background: linear-gradient(160deg, #35307c 0%, var(--brand-indigo) 55%, #29256a 100%);
  }
  .card--back .brand {
    left: 70px; top: 66px;
    color: var(--card-white);
    font-size: 30px;
  }
  .card--back .brand__mark { width: 18px; height: 18px; }
</style>
</head>
<body>
<main class="stage">

  <section class="card card--front" aria-label="Business card front">
    <div class="brand"><span class="brand__mark"></span>R Marlowe Consulting</div>

    <div class="holder">
      <div class="holder__name">Lucas Moreira</div>
      <div class="holder__role">MANAGING DIRECTOR</div>
    </div>

    <ul class="contacts">
      <li>
        <svg viewBox="0 0 14 14" aria-hidden="true"><circle cx="7" cy="7" r="7" fill="#1c1c24"/><path d="M4.6 3.8l1.3 1.3-.7.9c.5 1 1.3 1.8 2.3 2.3l.9-.7 1.3 1.3-.8.9c-2.3-.4-4.2-2.3-4.6-4.6z" fill="#fff"/></svg>
        +55-11-xxxx-xxxx
      </li>
      <li>
        <svg viewBox="0 0 14 14" aria-hidden="true"><circle cx="7" cy="7" r="7" fill="#1c1c24"/><rect x="3.5" y="4.5" width="7" height="5" fill="none" stroke="#fff" stroke-width="1"/><path d="M3.5 4.5l3.5 3 3.5-3" fill="none" stroke="#fff" stroke-width="1"/></svg>
        contact@rmarlowe.com
      </li>
      <li>
        <svg viewBox="0 0 14 14" aria-hidden="true"><circle cx="7" cy="7" r="7" fill="#1c1c24"/><circle cx="7" cy="7" r="3.6" fill="none" stroke="#fff" stroke-width="1"/><path d="M3.4 7h7.2M7 3.4c-1.6 2-1.6 5.2 0 7.2M7 3.4c1.6 2 1.6 5.2 0 7.2" fill="none" stroke="#fff" stroke-width=".8"/></svg>
        www.rmarlowe.com
      </li>
      <li>
        <svg viewBox="0 0 14 14" aria-hidden="true"><circle cx="7" cy="7" r="7" fill="#1c1c24"/><path d="M7 3.2a2.5 2.5 0 0 1 2.5 2.5C9.5 7.6 7 10.8 7 10.8S4.5 7.6 4.5 5.7A2.5 2.5 0 0 1 7 3.2z" fill="#fff"/><circle cx="7" cy="5.7" r=".9" fill="#1c1c24"/></svg>
        Dr. Olavo Brendim Av., 312
      </li>
      <li class="contacts__cont">- Tower II - 16th floor</li>
    </ul>

    <div class="edge-band" aria-hidden="true">
      <span class="edge-band__dark"></span>
      <span class="edge-band__color"></span>
    </div>
  </section>

  <section class="card card--back" aria-label="Business card back">
    <div class="brand"><span class="brand__mark"></span>R Marlowe Consulting</div>
  </section>

</main>
</body>
</html>
```